Business Card Project

We are a small consulting firm. You can experiment with any design.
Must have:
1) Company name - OLUNDEX International
2) Company slogan - simple solutions for complex problems
3) Name/Title/Phone/Email/WWW/ - use anything you like as an example.

Industry/Entity Type

Business

```html
<!DOCTYPE html>
<html lang="en">
<head>
<meta charset="utf-8">
<title>OLUNDEX International – Business Cards</title>
<link href="https://fonts.googleapis.com/css2?family=Open+Sans:wght@400;600;700&display=swap" rel="stylesheet">
<style>
  :root {
    --stage-light: #f2f2f2;
    --stage-dark: #c4c4c4;
    --sky: #80c6ea;
    --paper: #ffffff;
    --royal: #0063b1;
    --royal-soft: #2384c3;
    --charcoal: #252525;
    --charcoal-edge: #5f5f5f;
    --ink: #1f1f1f;
    --ink-edge: #333333;
    --text-grey: #555555;
    --text-mid: #9a9a9a;
    --brand-blue: #1e7fc6;
    --white: #ffffff;
  }
  * { margin: 0; padding: 0; box-sizing: border-box; }
  html, body { width: 1200px; height: 1000px; overflow: hidden; }
  body {
    position: relative;
    background: linear-gradient(135deg, var(--stage-light) 0%, #dcdcdc 55%, var(--stage-dark) 100%);
    font-family: "Open Sans", Arial, sans-serif;
  }
  .card {
    position: absolute;
    width: 530px;
    height: 304px;
    border-radius: 152px 0 0 152px;
    overflow: hidden;
  }
  .card--front-light { left: 60px; top: 178px; background: var(--sky); }
  .card--back-blue { left: 612px; top: 177px; width: 531px; height: 305px; background: var(--royal); }
  .card--front-dark { left: 60px; top: 512px; background: var(--charcoal-edge); }
  .card--back-dark { left: 612px; top: 512px; width: 531px; height: 306px; background: var(--ink); }

  .card__panel { position: absolute; left: 118px; top: 0; right: 0; bottom: 0; }
  .card--front-light .card__panel { background: var(--paper); }
  .card--front-dark .card__panel { background: var(--charcoal); }
  .card--back-blue .card__panel { left: 0; background: var(--royal-soft); width: 152px; border-radius: 152px 0 0 152px; height: 100%; }
  .card--back-dark .card__panel { left: 0; background: var(--ink-edge); width: 152px; border-radius: 152px 0 0 152px; height: 100%; }

  .brand { position: absolute; display: flex; align-items: center; gap: 10px; white-space: nowrap; }
  .brand__dot { width: 34px; height: 34px; border-radius: 50%; flex: none; }
  .brand__name { font-weight: 400; font-size: 17px; line-height: 19px; letter-spacing: 1px; }
  .brand__name span { display: block; }
  .card--front-light .brand, .card--front-dark .brand { left: 308px; top: 27px; }
  .card--front-light .brand__dot, .card--front-dark .brand__dot { background: var(--brand-blue); }
  .card--front-light .brand__name { color: var(--text-grey); }
  .card--front-dark .brand__name { color: var(--text-mid); }
  .card--back-blue .brand, .card--back-dark .brand { left: 284px; top: 131px; }
  .card--back-blue .brand__dot, .card--back-dark .brand__dot { background: var(--white); }
  .card--back-blue .brand__name, .card--back-dark .brand__name { color: var(--white); }

  .slogan { position: absolute; left: 311px; top: 73px; font-size: 11px; }
  .card--front-light .slogan { color: var(--text-grey); }
  .card--front-dark .slogan { color: var(--text-mid); }

  .role { position: absolute; font-size: 15px; }
  .person { position: absolute; font-size: 17px; font-weight: 700; }
  .card--front-light .role { left: 340px; top: 110px; color: var(--text-grey); }
  .card--front-light .person { left: 340px; top: 130px; color: var(--text-grey); }
  .card--front-dark .role { left: 410px; top: 104px; color: var(--text-mid); }
  .card--front-dark .person { left: 410px; top: 124px; color: var(--text-mid); }

  .contacts { position: absolute; list-style: none; font-size: 13px; line-height: 21.5px; }
  .card--front-light .contacts { left: 340px; top: 200px; color: var(--text-grey); }
  .card--front-dark .contacts { right: 26px; top: 196px; text-align: right; color: var(--text-mid); }
  .contacts .web { margin-top: 1px; }
</style>
</head>
<body>

  <section class="card card--front-light">
    <div class="card__panel"></div>
    <div class="brand"><span class="brand__dot"></span><span class="brand__name"><span>OLUNDEX</span><span>International</span></span></div>
    <p class="slogan">Simple solutions for complex problems</p>
    <p class="role">CEO:</p>
    <p class="person">Maren Quist</p>
    <ul class="contacts">
      <li>P: 000 0000 0000</li>
      <li>F: 000 0000 0000</li>
      <li>E: hello@olundex.com</li>
      <li class="web">www.olundex.com</li>
    </ul>
  </section>

  <section class="card card--back-blue">
    <div class="card__panel"></div>
    <div class="brand"><span class="brand__dot"></span><span class="brand__name"><span>OLUNDEX</span><span>International</span></span></div>
  </section>

  <section class="card card--front-dark">
    <div class="card__panel"></div>
    <div class="brand"><span class="brand__dot"></span><span class="brand__name"><span>OLUNDEX</span><span>International</span></span></div>
    <p class="slogan">Simple solutions for complex problems</p>
    <p class="role">CEO:</p>
    <p class="person">Maren Quist</p>
    <ul class="contacts">
      <li>P: 000 0000 0000</li>
      <li>F: 000 0000 0000</li>
      <li>E: hello@olundex.com</li>
      <li class="web">www.olundex.com</li>
    </ul>
  </section>

  <section class="card card--back-dark">
    <div class="card__panel"></div>
    <div class="brand"><span class="brand__dot"></span><span class="brand__name"><span>OLUNDEX</span><span>International</span></span></div>
  </section>

</body>
</html>
```